Business Card for TKR, logo files already created

Please, can you assist with creating a Business card the TKR graphics which are already listed on www.tarnkeyrelay.example
The business card should be modern and upmarket, textured designs are welcome. Please feel free to express yourself and be very bold with your design.

Target Market(s)

Cyber Security

Industry/Entity Type

Information Technology

Contact Information for Business Card

Company Name
Name
Title
Mobile
Fax or Tel
email
url

Font styles to use
Serif
Sans Serif

Colors
3277b5
85acd3
ffffff

```html
<!DOCTYPE html>
<html lang="en">
<head>
<meta charset="utf-8">
<title>TKR Business Card</title>
<link href="https://fonts.googleapis.com/css2?family=Michroma&family=Roboto:wght@400&display=swap" rel="stylesheet">
<style>
  :root{
    --bg:#2b2b2d;
    --card-white:#ffffff;
    --card-black:#050505;
    --brand-blue:#3447a6;
    --soft-blue:#5a6fc4;
    --text-light:#e6e6e6;
    --rule-grey:#8a8a8a;
  }
  html,body{margin:0;padding:0;overflow:hidden;}
  body{width:1200px;height:927px;background:var(--bg);position:relative;font-family:"Roboto",Arial,sans-serif;}
  .card{position:absolute;width:600px;height:343px;box-shadow:0 18px 40px rgba(0,0,0,.45);overflow:hidden;}
  .card--front{left:60px;top:70px;background:var(--card-white);}
  .card--back{left:540px;top:480px;background:var(--card-black);}

  .brand{position:absolute;text-align:center;font-family:"Michroma",Arial,sans-serif;color:var(--brand-blue);}
  .brand__mark{font-size:64px;letter-spacing:4px;line-height:1;}
  .brand__name{font-size:19px;letter-spacing:1px;margin-top:8px;line-height:1;}
  .brand__sub{font-size:12px;letter-spacing:2px;margin-top:6px;line-height:1;}
  .brand__rule{height:1px;background:var(--rule-grey);margin:8px 0 7px;}
  .brand__tagline{font-size:10px;letter-spacing:1.2px;line-height:1;}

  .card--front .brand{left:150px;top:62px;width:300px;}
  .front__band{position:absolute;left:0;right:0;top:255px;height:34px;background:var(--brand-blue);
    color:#fff;font-family:"Michroma",Arial,sans-serif;font-size:12px;letter-spacing:1.5px;
    display:flex;align-items:center;justify-content:center;}

  .card--back .brand{right:40px;top:34px;width:262px;}
  .card--back .brand__mark{font-size:56px;}
  .card--back .brand__name{font-size:17px;}
  .card--back .brand__sub{font-size:11px;}
  .card--back .brand__tagline{font-size:9px;}

  .person{position:absolute;left:34px;top:92px;font-family:"Michroma",Arial,sans-serif;}
  .person__name{color:var(--soft-blue);font-size:18px;letter-spacing:1px;}
  .person__title{color:var(--text-light);font-size:11px;letter-spacing:1px;margin-top:6px;}

  .contact{position:absolute;color:var(--text-light);font-size:14px;line-height:20px;}
  .contact__row{display:flex;align-items:center;gap:8px;}
  .contact__row svg{width:13px;height:13px;flex:none;}
  .contact--web{right:30px;top:198px;width:300px;border-top:1px solid var(--rule-grey);padding-top:6px;text-align:right;}
  .contact--web .contact__row{justify-content:flex-end;}
  .contact--phone{left:34px;top:258px;width:230px;border-top:1px solid var(--rule-grey);padding-top:6px;}
  .back__band{position:absolute;left:0;right:0;bottom:0;height:12px;background:var(--brand-blue);}
</style>
</head>
<body>

<section class="card card--front" aria-label="Business card front">
  <div class="brand">
    <div class="brand__mark">TKR</div>
    <div class="brand__name">TARNKEY RELAY</div>
    <div class="brand__sub">SOLUTIONS</div>
    <div class="brand__rule"></div>
    <div class="brand__tagline">INTELLIGENCE - DRIVEN SOLUTIONS</div>
  </div>
  <div class="front__band">WWW.TARNKEYRELAY.EXAMPLE</div>
</section>

<section class="card card--back" aria-label="Business card back">
  <div class="person">
    <div class="person__name">MARCUS HALE</div>
    <div class="person__title">CEO/FOUNDER</div>
  </div>

  <div class="brand">
    <div class="brand__mark">TKR</div>
    <div class="brand__name">TARNKEY RELAY</div>
    <div class="brand__sub">SOLUTIONS</div>
    <div class="brand__rule"></div>
    <div class="brand__tagline">INTELLIGENCE - DRIVEN SOLUTIONS</div>
  </div>

  <div class="contact contact--web">
    <div class="contact__row">marcushale@tarnkeyrelay.example
      <svg viewBox="0 0 16 16" aria-hidden="true"><rect x="1" y="3" width="14" height="10" fill="none" stroke="#5a6fc4" stroke-width="1.5"/><path d="M1 3l7 6 7-6" fill="none" stroke="#5a6fc4" stroke-width="1.5"/></svg>
    </div>
    <div class="contact__row">www.tarnkeyrelay.example
      <svg viewBox="0 0 16 16" aria-hidden="true"><circle cx="8" cy="8" r="6.5" fill="none" stroke="#5a6fc4" stroke-width="1.5"/><path d="M1.5 8h13M8 1.5v13M3 4.5h10M3 11.5h10" fill="none" stroke="#5a6fc4" stroke-width="1"/></svg>
    </div>
  </div>

  <div class="contact contact--phone">
    <div class="contact__row">
      <svg viewBox="0 0 16 16" aria-hidden="true"><path d="M3 1.5l3 3-1.5 2c1 2 3 4 5 5l2-1.5 3 3-2 2C7 14 2 9 1 3.5z" fill="#5a6fc4"/></svg>555-014-2270
    </div>
    <div class="contact__row">
      <svg viewBox="0 0 16 16" aria-hidden="true"><rect x="4" y="1" width="8" height="14" rx="1.5" fill="none" stroke="#5a6fc4" stroke-width="1.5"/><circle cx="8" cy="12.5" r="0.9" fill="#5a6fc4"/></svg>555-014-2270
    </div>
  </div>

  <div class="back__band"></div>
</section>

</body>
</html>
```